Migration Lawyers

Company: Dunstan & Co Lawyers & Migration Agents

Name: Graham Dunstan BEc, LLB
Address: Level 18, 72 Hollis Street
Sydney, NSW, Australia 2000

Ph: +61 2 9384 5207
M: 0428316540
E: graham@permitpath-example.org.au
W: www.permitpath-example.org.au

Target Market(s)

Migration Clients

Industry/Entity Type

It Company

Font styles to use
Script

Requirements
Must have
• Logo
Should not have
• Please scale the format to the printing size attached

```html
<!DOCTYPE html>
<html lang="en">
<head>
<meta charset="UTF-8">
<title>Dunstan &amp; Co — Business Card</title>
<link rel="stylesheet" href="https://fonts.googleapis.com/css2?family=Tinos:wght@400;700&display=swap">
<style>
  :root {
    --stage: #121212;
    --paper: #ffffff;
    --navy: #12336a;
    --ink: #111111;
    --hairline: #8a96b8;
  }
  * { margin: 0; padding: 0; box-sizing: border-box; }
  html, body { width: 999px; height: 1200px; overflow: hidden; background: var(--stage); }
  body { position: relative; font-family: "Tinos", "Times New Roman", serif; }

  .card { position: absolute; width: 917px; height: 520px; overflow: hidden; }
  .card-front { left: 42px; top: 56px; background: var(--paper); }
  .card-back { left: 37px; top: 643px; background: var(--navy); }
  .wave { position: absolute; inset: 0; width: 100%; height: 100%; }

  .holder-name { position: absolute; right: 26px; top: 38px; font-weight: 700; font-size: 23px; color: var(--navy); letter-spacing: 0.3px; }
  .holder-degree { position: absolute; left: 736px; top: 66px; width: 104px; text-align: center; font-weight: 700; font-size: 23px; color: var(--ink); }

  .brand { position: absolute; left: 214px; top: 146px; display: flex; align-items: center; gap: 18px; }
  .brand-mark { width: 170px; height: 158px; border: 1.5px solid var(--navy); border-radius: 50%; flex: none; }
  .brand-name { color: var(--navy); font-weight: 700; line-height: 1; }
  .brand-name .firm { display: block; font-size: 52px; }
  .brand-name .practice { display: block; font-size: 21px; margin-top: 8px; }

  .contact { position: absolute; color: var(--paper); font-size: 25px; display: flex; align-items: center; white-space: nowrap; }
  .contact svg { width: 20px; height: 20px; flex: none; fill: none; stroke: var(--paper); stroke-width: 1.8; }
  .contact-address { left: 120px; top: 152px; gap: 10px; }
  .contact-line { left: 296px; gap: 22px; }
  .contact-phone { top: 202px; }
  .contact-mobile { top: 245px; }
  .contact-email { top: 285px; }
  .contact-web { top: 325px; }
</style>
</head>
<body>

<section class="card card-front">
  <svg class="wave" viewBox="0 0 1102 625" preserveAspectRatio="none" aria-hidden="true">
    <path d="M0 335 C220 370 420 560 570 561 C760 565 930 436 1102 436 L1102 625 L0 625 Z" fill="var(--navy)"/>
    <path d="M0 398 C200 410 400 575 570 575 C760 575 930 480 1102 478" fill="none" stroke="var(--hairline)" stroke-width="1"/>
  </svg>
  <div class="holder-name">GRAHAM DUNSTAN</div>
  <div class="holder-degree">BEc, LLB</div>
  <div class="brand">
    <div class="brand-mark"></div>
    <div class="brand-name">
      <span class="firm">Dunstan &amp; Co</span>
      <span class="practice">Lawyers &amp; Migration Agents</span>
    </div>
  </div>
</section>

<section class="card card-back">
  <svg class="wave" viewBox="0 0 1103 626" preserveAspectRatio="none" aria-hidden="true">
    <path d="M0 438 C200 440 400 570 560 563 C780 555 900 350 1103 335 L1103 626 L0 626 Z" fill="var(--paper)"/>
    <path d="M0 478 C200 480 380 590 560 576 C760 560 920 400 1103 398" fill="none" stroke="var(--hairline)" stroke-width="1"/>
  </svg>

  <div class="contact contact-address">
    <svg viewBox="0 0 20 20"><path d="M10 19 C10 19 4 11 4 7.5 A6 6 0 0 1 16 7.5 C16 11 10 19 10 19 Z" fill="var(--paper)" stroke="none"/><circle cx="10" cy="7.5" r="2.2" fill="var(--navy)" stroke="none"/></svg>
    <span>Level 18, 72 Hollis Street, Australia, Sydney, NSW, 2000</span>
  </div>
  <div class="contact contact-line contact-phone">
    <svg viewBox="0 0 20 20"><circle cx="10" cy="10" r="8"/><path d="M8 6 C11 7 11 13 8 14"/></svg>
    <span>+61 2 9384 5207</span>
  </div>
  <div class="contact contact-line contact-mobile">
    <svg viewBox="0 0 20 20"><rect x="6" y="3" width="8" height="15" rx="1"/><line x1="7" y1="1" x2="7" y2="3"/><line x1="8" y1="11" x2="12" y2="11"/><line x1="8" y1="14" x2="12" y2="14"/></svg>
    <span>0428316540</span>
  </div>
  <div class="contact contact-line contact-email">
    <svg viewBox="0 0 20 20"><rect x="2" y="5" width="16" height="10"/><path d="M2 5 L10 11 L18 5"/></svg>
    <span>graham@permitpath-example.org.au</span>
  </div>
  <div class="contact contact-line contact-web">
    <svg viewBox="0 0 20 20"><circle cx="10" cy="10" r="8"/><ellipse cx="10" cy="10" rx="3.5" ry="8"/><line x1="2" y1="10" x2="18" y2="10"/></svg>
    <span>www.permitpath-example.org.au</span>
  </div>
</section>

</body>
</html>
```